Management consultant needs to update look of website

Currently I have a great word press website but it needs an updated look. I have new text for the site in the attached word document. I also have a list of websites whose design, look, and organization i like as a guide for the designer. The final design should be simple, strong, clear, and project the idea that my brand is a powerful authority in this space. Current site = www.brookfernadvisory.com

Target Market(s)

company owners / executives

Industry/Entity Type

Management Consulting

Number of Pages Required

3 page

Font styles to use
Serif

Colors

Designer to choose colors to be used in the design.

Requirements
Must have
• a simple and clear design and message. professional look. easy navigation. responsive to mobile devices. an easily implemented wordpress theme OR squarespace. use of my logo colors. though I am open to changing to a deep navy or charcoal logo image. source file uploaded.
Nice to have
• i like the cover photo and logo watermark on my current homepage. i like the google map with my logo on the current contact page. i like the animation as well. a great blend of the current site and something that is more seamless.

```html
<!DOCTYPE html>
<html lang="en">
<head>
<meta charset="utf-8">
<title>Brookfern Advisory</title>
<link href="https://fonts.googleapis.com/css2?family=Lato:wght@400;700;900&display=swap" rel="stylesheet">
<style>
:root{
  --gold:#c29a3c;
  --gold-light:#d9b760;
  --gold-dark:#a87a22;
  --ink:#3a3a3a;
  --text:#4a4a4a;
  --white:#ffffff;
  --charcoal:#2d2d2d;
  --footer:#2a2a2a;
  --logo-grey:#8a8a8a;
}
*{margin:0;padding:0;box-sizing:border-box}
html,body{width:1200px;height:2835px;overflow:hidden}
body{font-family:'Lato',sans-serif;color:var(--text);background:var(--white);position:relative}
.hero{position:absolute;left:0;top:0;width:1200px;height:733px;
  background:linear-gradient(160deg,#6c6e72 0%,#4d5158 40%,#3d4249 70%,#55585c 100%)}
.hero-shade{position:absolute;inset:0;background:rgba(25,25,30,.35)}
.nav{position:absolute;top:0;left:0;width:1200px;height:110px}
.brand{position:absolute;left:160px;top:36px;display:flex;align-items:center;gap:14px}
.brand-mark{width:44px;height:44px;border-radius:50%;background:var(--gold)}
.brand-name{font-weight:700;font-size:27px;color:var(--gold);letter-spacing:.5px}
.menu{position:absolute;top:44px;right:165px;display:flex;gap:34px;list-style:none}
.menu li{font-size:16px;font-weight:700;color:var(--white);letter-spacing:.3px}
.menu li.active{color:var(--gold-light)}
.hero-title{position:absolute;top:322px;width:1200px;text-align:center;color:var(--white);font-weight:900;text-transform:uppercase}
.hero-title .l1{display:block;font-size:46px;line-height:54px}
.hero-title .l2{display:block;font-size:36px;line-height:46px;font-weight:700}
.notch{position:absolute;left:0;width:1200px}
.intro{position:absolute;top:834px;left:210px;width:780px;text-align:center;font-size:20px;line-height:30px;color:var(--text)}
.intro p+p{margin-top:16px}
.testimonials{position:absolute;left:0;top:1170px;width:1200px;height:425px}
.t-inner{position:absolute;top:70px;left:190px;width:820px;text-align:center;color:var(--white)}
.t-title{font-size:27px;font-weight:900;letter-spacing:.5px}
.t-quote{font-size:60px;font-weight:700;line-height:50px;margin-top:18px;font-style:normal}
.t-text{font-size:18px;line-height:27px;margin-top:6px}
.t-name{font-size:18px;font-weight:900;margin-top:16px}
.clients-title{position:absolute;top:1662px;width:1200px;text-align:center;font-size:27px;font-weight:900;color:#222}
.clients{position:absolute;top:1760px;left:150px;width:900px;display:grid;grid-template-columns:repeat(5,180px);grid-template-rows:130px 130px 150px}
.client{display:flex;align-items:center;justify-content:center;font-size:21px;font-weight:700;color:var(--logo-grey)}
.cta{position:absolute;left:0;top:2235px;width:1200px;height:525px;
  background:linear-gradient(120deg,#3b3b3b 0%,#2f3032 45%,#4a4a4a 100%)}
.cta-inner{position:absolute;top:88px;width:1200px;text-align:center;color:var(--white)}
.cta-title{font-size:31px;font-weight:900;line-height:38px;text-transform:uppercase}
.cta-sub{font-size:17px;line-height:25px;margin:16px auto 0;width:700px}
.form{position:absolute;top:272px;left:178px;display:flex;gap:10px}
.field{width:277px;height:50px;background:var(--white);color:#555;font-size:17px;padding:0 20px;display:flex;align-items:center}
.btn{width:276px;height:50px;background:var(--gold);color:var(--white);font-size:17px;font-weight:700;display:flex;align-items:center;justify-content:center}
.cta-note{position:absolute;top:368px;width:1200px;text-align:center;font-size:16px;line-height:24px;color:#ddd}
.social{position:absolute;top:434px;left:518px;display:flex;gap:12px}
.social span{width:44px;height:44px;border:2px solid var(--white);border-radius:50%}
.footer{position:absolute;top:2760px;left:0;width:1200px;height:75px;background:var(--footer);color:#bbb;font-size:14px;text-align:center;line-height:75px}
</style>
</head>
<body>
<header class="hero">
  <div class="hero-shade" role="img" aria-label="Photo of a presenter leading a workshop with business people at a meeting table"></div>
  <nav class="nav">
    <div class="brand"><span class="brand-mark"></span><span class="brand-name">BROOKFERN ADVISORY</span></div>
    <ul class="menu"><li class="active">HOME</li><li>ABOUT</li><li>SERVICES</li><li>ARTICLES</li><li>CONTACT</li></ul>
  </nav>
  <h1 class="hero-title"><span class="l1">Great companies succeed by</span><span class="l2">Investing in the right people</span></h1>
</header>
<svg class="notch" style="top:690px" width="1200" height="50" viewBox="0 0 1200 50">
  <path d="M0 43 H545 C570 43 580 20 600 20 C620 20 630 43 655 43 H1200 V50 H0Z" fill="#fff"/>
  <path d="M600 22 V42 M592 34 L600 42 L608 34" stroke="#777" stroke-width="2" fill="none"/>
</svg>
<section class="intro">
  <p>It’s no secret that long-term business success requires a smart investment in the right people for your company. And yet, knowing how to cultivate a strong staff and keep them focused on the road ahead can be challenging for even the savviest organizational leaders and human resource executives.</p>
  <p>I’m Dr. Elena Marsh and I want to help business owners, leaders, and HR teams understand how to identify, develop, and retain talented professionals who can take your success to the next level.</p>
</section>
<section class="testimonials">
  <svg width="1200" height="425" viewBox="0 0 1200 425" style="position:absolute;left:0;top:0">
    <defs><linearGradient id="gold" x1="0" y1="0" x2="1" y2="1">
      <stop offset="0" stop-color="#d6b45c"/><stop offset=".55" stop-color="#c29a3c"/><stop offset="1" stop-color="#a87a22"/></linearGradient></defs>
    <path d="M0 5 H550 C575 5 580 35 600 35 C620 35 625 5 650 5 L1200 11 V421 L0 414Z" fill="url(#gold)"/>
    <circle cx="601" cy="8" r="18" fill="#fff"/>
    <circle cx="601" cy="8" r="12" fill="none" stroke="#c29a3c" stroke-width="3"/>
    <path d="M128 192 L98 222 L128 252 M1072 192 L1102 222 L1072 252" stroke="#fff" stroke-width="2.5" fill="none"/>
  </svg>
  <div class="t-inner">
    <h2 class="t-title">TESTIMONIALS</h2>
    <div class="t-quote">“</div>
    <p class="t-text">After working in the consulting business for 12 years, I met Elena. I was immediately impressed by her ability to ask the right questions. It is rare to find someone with her credentials who also continues to have deep curiosity and creativity about their area of expertise. Elena has a passion for helping people reach their full potential from the classroom to c-suite and Brookfern Advisory is a powerful platform to push people to their personal best.</p>
    <p class="t-name">MAREN T</p>
  </div>
</section>
<h2 class="clients-title">CLIENTS &amp; PARTNERS</h2>
<section class="clients">
  <div class="client">Harbor Guild</div><div class="client">Pinecrest</div><div class="client">Foldline</div><div class="client">Oakhand</div><div class="client">Clearway</div>
  <div class="client">Ridgepoint</div><div class="client">Kestrel</div><div class="client">Venture Hub</div><div class="client">Elm Club</div><div class="client">Hale &amp; Partners</div>
  <div class="client">Whole Self</div><div class="client">Lumen TV</div><div class="client">Veralink</div><div class="client">Tierra Media</div><div class="client">Orbis Cast</div>
</section>
<section class="cta" role="img" aria-label="Photo of a speaker presenting to a seated audience">
  <div class="cta-inner">
    <h2 class="cta-title">Learn to inspire employees and unlock<br>their maximum potential</h2>
    <p class="cta-sub">If you’re struggling to connect with today’s employees and you need to develop a better way to lead them, I want to help you become the very best leader possible.</p>
  </div>
  <div class="form"><div class="field">First Name</div><div class="field">Email address</div><div class="btn">Download Free Information</div></div>
  <p class="cta-note">You’ll receive monthly updates filled with leader-focused resources and helpful information that<br>will help you build stronger organizational leaders. You can unsubscribe at any time.</p>
  <div class="social"><span aria-label="Social link"></span><span aria-label="Social link"></span><span aria-label="Social link"></span></div>
</section>
<svg class="notch" style="top:2228px" width="1200" height="45" viewBox="0 0 1200 45">
  <path d="M550 7 C575 7 580 36 600 36 C620 36 625 7 650 7Z" fill="#fff"/>
  <circle cx="600" cy="6" r="18" fill="#fff"/>
  <circle cx="600" cy="6" r="12" fill="none" stroke="#c29a3c" stroke-width="3"/>
</svg>
<footer class="footer">© 2019 Company Name &nbsp;All right reserved</footer>
</body>
</html>
```